Re-Design the flow of the Orvane Framework

The orvane framework is a 10 step model that helps teams/organizations become high performing. Attached the model which i created. I love the design as it is but i used a template i don't owe the rights of so i would like to use this platform to see what you can come up with the redesign this flow while keeping the key elements in place. I like the flow, i like the cleanness and i like it to be compact.

Target Market(s)

Organizational change / Leadership/ Consultancy

Industry/Entity Type

Leadership

Requirements
Must have
• Keep as much as possible the flow and feel of the attached
Nice to have
• -Maybe some twist in how the different parts connect (not a must)
Should not have
• Less or more steps than added in the attached file

```html
<!DOCTYPE html>
<html lang="en">
<head>
<meta charset="utf-8">
<title>The Orvane Framework</title>
<link href="https://fonts.googleapis.com/css2?family=Archivo+Black&family=Source+Sans+3:wght@400;600;700&display=swap" rel="stylesheet">
<style>
  :root {
    --bg: #6d6658;
    --paper: #ffffff;
    --ink-dark: #5a5448;
    --tan: #b89a6e;
    --blue: #4474b8;
    --navy: #323a8c;
    --violet: #5b2d8e;
    --sky: #5fa8df;
    --teal: #58a89c;
    --lime: #a4c64a;
    --plum: #7b2d90;
    --magenta: #b82260;
    --vermilion: #d65a30;
    --amber: #e0922e;
  }
  html, body { margin: 0; padding: 0; width: 1200px; height: 840px; overflow: hidden; background: var(--bg); }
  .canvas { width: 1200px; height: 840px; display: block; background: var(--bg); }

  .tile { fill: var(--paper); stroke: var(--bg); stroke-width: 7; stroke-linejoin: round; }
  .core { stroke: var(--bg); stroke-width: 7; stroke-linejoin: round; }

  .step-text { font-family: "Source Sans 3", Arial, sans-serif; font-weight: 600; font-size: 13px; text-anchor: middle; }
  .hub-title { font-family: "Source Sans 3", Arial, sans-serif; font-weight: 700; font-size: 12px; letter-spacing: .6px; fill: var(--paper); text-anchor: middle; }
  .path-label { font-family: "Source Sans 3", Arial, sans-serif; font-weight: 600; font-size: 15px; letter-spacing: 2.5px; fill: var(--paper); }
  .outcome-title { font-family: "Source Sans 3", Arial, sans-serif; font-weight: 700; font-size: 14px; fill: var(--ink-dark); text-anchor: middle; }
  .outcome-list { font-family: "Source Sans 3", Arial, sans-serif; font-weight: 400; font-size: 11.5px; fill: var(--ink-dark); }
  .brand-title { font-family: "Archivo Black", Arial, sans-serif; font-size: 40px; fill: var(--paper); }
  .brand-title .accent { fill: var(--tan); }
  .brand-tagline { font-family: "Source Sans 3", Arial, sans-serif; font-size: 12px; fill: var(--paper); letter-spacing: .2px; }

  .icon-line { fill: none; stroke: var(--paper); stroke-width: 3; stroke-linecap: round; stroke-linejoin: round; }
  .icon-fill { fill: var(--paper); }
  .flow-arrow { fill: var(--paper); }
</style>
</head>
<body>
<svg class="canvas" viewBox="0 0 1200 840" xmlns="http://www.w3.org/2000/svg">
  <defs>
    <symbol id="heart-pulse" viewBox="0 0 100 100">
      <path d="M50 90 L13 52 A22 22 0 0 1 50 20 A22 22 0 0 1 87 52 Z" fill="#fff"/>
      <polyline points="20,54 36,54 42,42 50,68 57,44 63,54 80,54" fill="none" stroke="currentColor" stroke-width="6" stroke-linejoin="round" stroke-linecap="round"/>
    </symbol>
    <path id="arc-self-direction" d="M72.3,532.1 A300 300 0 0 1 72.3,187.9"/>
    <path id="arc-human-experience" d="M215.4,78.1 A300 300 0 0 1 577.8,210"/>
    <path id="arc-unleash-engagement" d="M639.2,667 A278 278 0 0 0 1120.8,667"/>
  </defs>

  <!-- Foundation wheel: six steps, clockwise from the bottom -->
  <g class="foundation-wheel">
    <path class="tile" d="M460.5,606.8 A285 285 0 0 1 175.5,606.8 L249,479.5 A138 138 0 0 0 387,479.5 Z"/>
    <path class="tile" d="M175.5,606.8 A285 285 0 0 1 33,360 L180,360 A138 138 0 0 0 249,479.5 Z"/>
    <path class="tile" d="M33,360 A285 285 0 0 1 175.5,113.2 L249,240.5 A138 138 0 0 0 180,360 Z"/>
    <path class="tile" d="M175.5,113.2 A285 285 0 0 1 460.5,113.2 L387,240.5 A138 138 0 0 0 249,240.5 Z"/>
    <path class="tile" d="M460.5,113.2 A285 285 0 0 1 603,360 L456,360 A138 138 0 0 0 387,240.5 Z"/>
    <path class="tile" d="M603,360 A285 285 0 0 1 460.5,606.8 L387,479.5 A138 138 0 0 0 456,360 Z"/>

    <path class="core" fill="var(--lime)" d="M387,479.5 A138 138 0 0 1 249,479.5 L277,431 A82 82 0 0 0 359,431 Z"/>
    <path class="core" fill="var(--teal)" d="M249,479.5 A138 138 0 0 1 180,360 L236,360 A82 82 0 0 0 277,431 Z"/>
    <path class="core" fill="var(--sky)" d="M180,360 A138 138 0 0 1 249,240.5 L277,289 A82 82 0 0 0 236,360 Z"/>
    <path class="core" fill="var(--blue)" d="M249,240.5 A138 138 0 0 1 387,240.5 L359,289 A82 82 0 0 0 277,289 Z"/>
    <path class="core" fill="var(--navy)" d="M387,240.5 A138 138 0 0 1 456,360 L400,360 A82 82 0 0 0 359,289 Z"/>
    <path class="core" fill="var(--violet)" d="M456,360 A138 138 0 0 1 387,479.5 L359,431 A82 82 0 0 0 400,360 Z"/>

    <!-- icons -->
    <g class="icon-compass">
      <circle class="icon-line" cx="318" cy="470" r="13"/>
      <polygon class="icon-fill" points="318,460 322,470 318,480 314,470"/>
    </g>
    <g class="icon-eye">
      <path class="icon-line" d="M207,415 Q223,401 239,415 Q223,429 207,415 Z"/>
      <circle class="icon-fill" cx="223" cy="415" r="4.5"/>
    </g>
    <g class="icon-target">
      <circle class="icon-line" cx="223" cy="305" r="12"/>
      <circle class="icon-line" cx="223" cy="305" r="5.5"/>
      <line class="icon-line" x1="223" y1="288" x2="223" y2="293"/>
      <line class="icon-line" x1="223" y1="317" x2="223" y2="322"/>
      <line class="icon-line" x1="206" y1="305" x2="211" y2="305"/>
      <line class="icon-line" x1="235" y1="305" x2="240" y2="305"/>
    </g>
    <g class="icon-shield">
      <path class="icon-line" d="M318,236 L331,241 V251 Q331,262 318,267 Q305,262 305,251 V241 Z"/>
      <polyline class="icon-line" points="312,251 316,255 324,246"/>
    </g>
    <use href="#heart-pulse" x="397" y="289" width="32" height="32" style="color: var(--navy)"/>
    <g class="icon-growth">
      <polyline class="icon-line" points="399,425 408,416 414,421 427,407"/>
      <polyline class="icon-line" points="420,407 427,407 427,414"/>
    </g>

    <text class="hub-title" x="318" y="346">CAPABILITIES</text>
    <text class="hub-title" x="318" y="364">DRIVING A SOLID</text>
    <text class="hub-title" x="318" y="382">FOUNDATION</text>
  </g>

  <!-- Link between the two phases -->
  <polygon class="flow-arrow" points="600,437 619,450 600,463"/>

  <!-- Excellence channel: four steps, down, across and up -->
  <g class="excellence-channel">
    <rect class="tile" x="630" y="370" width="118" height="158"/>
    <path class="tile" d="M630,528 A250 250 0 0 0 880,778 L880,660 A132 132 0 0 1 748,528 Z"/>
    <path class="tile" d="M880,778 A250 250 0 0 0 1130,528 L1012,528 A132 132 0 0 1 880,660 Z"/>
    <rect class="tile" x="1012" y="370" width="118" height="158"/>

    <rect class="core" fill="var(--plum)" x="748" y="370" width="52" height="158"/>
    <path class="core" fill="var(--magenta)" d="M748,528 A132 132 0 0 0 880,660 L880,608 A80 80 0 0 1 800,528 Z"/>
    <path class="core" fill="var(--vermilion)" d="M880,660 A132 132 0 0 0 1012,528 L960,528 A80 80 0 0 1 880,608 Z"/>
    <rect class="core" fill="var(--amber)" x="960" y="370" width="52" height="158"/>

    <path class="icon-fill" d="M762,437 h24 a4 4 0 0 1 4 4 v14 a4 4 0 0 1 -4 4 h-14 l-7 6 v-6 h-3 a4 4 0 0 1 -4 -4 v-14 a4 4 0 0 1 4 -4 Z"/>
    <g class="icon-bottom-up">
      <line class="icon-line" x1="805" y1="614" x2="805" y2="591"/>
      <polyline class="icon-line" points="797,599 805,591 813,599"/>
      <line class="icon-line" x1="795" y1="619" x2="815" y2="619"/>
    </g>
    <g class="icon-trophy">
      <path class="icon-fill" d="M945,589 h20 v8 a10 10 0 0 1 -20 0 Z"/>
      <path class="icon-line" d="M945,592 h-5 v3 a6 6 0 0 0 6 6 M965,592 h5 v3 a6 6 0 0 1 -6 6" stroke-width="2.5"/>
      <rect class="icon-fill" x="952" y="606" width="6" height="6"/>
      <rect class="icon-fill" x="946" y="611" width="18" height="4"/>
    </g>
    <g class="icon-monitor">
      <circle class="icon-line" cx="982" cy="445" r="10"/>
      <polyline class="icon-line" points="975,446 979,446 981,441 984,450 986,446 989,446" stroke-width="2"/>
      <line class="icon-line" x1="989.5" y1="452.5" x2="997" y2="460" stroke-width="4"/>
    </g>

    <text class="hub-title" x="880" y="456">CAPABILITIES</text>
    <text class="hub-title" x="880" y="474">MAXIMIZING</text>
    <text class="hub-title" x="880" y="492">EXCELLENCE</text>
  </g>

  <!-- Outcome: the arrow the channel rises into -->
  <g class="outcome">
    <polygon class="flow-arrow" points="948,142 1070,64 1192,142"/>
    <rect fill="var(--paper)" x="962" y="150" width="216" height="212"/>
    <circle cx="1070" cy="192" r="20" fill="var(--bg)"/>
    <polygon points="1059,188 1064,181 1076,181 1081,188 1070,202" fill="none" stroke="#fff" stroke-width="2" stroke-linejoin="round"/>
    <line x1="1059" y1="188" x2="1081" y2="188" stroke="#fff" stroke-width="2"/>
    <text class="outcome-title" x="1070" y="238">Reaching full potential of</text>
    <text class="outcome-title" x="1070" y="256">people and organization</text>
    <text class="outcome-list">
      <tspan x="982" y="285">•Productivity up to 800%</tspan>
      <tspan x="982" y="302">•Employee engagement &gt;90%</tspan>
      <tspan x="982" y="319">•Max discretionary effort gap</tspan>
      <tspan x="982" y="336">•High resilience to change</tspan>
    </text>
  </g>

  <!-- Step labels -->
  <g class="step-labels">
    <text class="step-text" fill="var(--lime)"><tspan x="318" y="564">Discover you</tspan><tspan x="318" y="580">purpose. Why</tspan><tspan x="318" y="596">Do you exist?</tspan></text>
    <text class="step-text" fill="var(--teal)"><tspan x="132" y="448">Identify</tspan><tspan x="132" y="464">Purpose</tspan><tspan x="132" y="480">Activators</tspan><tspan x="132" y="496">(Vision)</tspan></text>
    <text class="step-text" fill="var(--sky)"><tspan x="132" y="241">Develop a</tspan><tspan x="132" y="257">Master plan</tspan><tspan x="132" y="273">(strategy)</tspan></text>
    <text class="step-text" fill="var(--blue)"><tspan x="318" y="126">Cultivate</tspan><tspan x="318" y="142">Psychological</tspan><tspan x="318" y="158">Safety and</tspan><tspan x="318" y="174">Ownership</tspan></text>
    <text class="step-text" fill="var(--navy)"><tspan x="504" y="233">Tap into peoples</tspan><tspan x="504" y="249">Purpose and</tspan><tspan x="504" y="265">Passion (intrinsic</tspan><tspan x="504" y="281">motivation)</tspan></text>
    <text class="step-text" fill="var(--violet)"><tspan x="504" y="440">Unlock</tspan><tspan x="504" y="456">culture of</tspan><tspan x="504" y="472">personal</tspan><tspan x="504" y="488">growth &amp;</tspan><tspan x="504" y="504">development</tspan></text>
    <text class="step-text" fill="var(--plum)"><tspan x="689" y="438">Prioritize</tspan><tspan x="689" y="454">Feedback &amp;</tspan><tspan x="689" y="470">Transparency</tspan></text>
    <text class="step-text" fill="var(--magenta)"><tspan x="746" y="651">Empower the</tspan><tspan x="746" y="667">community from</tspan><tspan x="746" y="683">bottom - up</tspan></text>
    <text class="step-text" fill="var(--vermilion)"><tspan x="1014" y="642">Put excellent</tspan><tspan x="1014" y="658">(team)</tspan><tspan x="1014" y="674">performance in</tspan><tspan x="1014" y="690">the spotlight</tspan></text>
    <text class="step-text" fill="var(--amber)"><tspan x="1071" y="438">Monitor</tspan><tspan x="1071" y="454">engagement</tspan><tspan x="1071" y="470">Real - time</tspan></text>
  </g>

  <!-- Flow labels following the shapes -->
  <g class="path-labels">
    <text class="path-label"><textPath href="#arc-self-direction" startOffset="50%" text-anchor="middle">SELF DIRECTION →</textPath></text>
    <text class="path-label"><textPath href="#arc-human-experience" startOffset="50%" text-anchor="middle">HUMANEXPERIENCE →</textPath></text>
    <text class="path-label"><textPath href="#arc-unleash-engagement" startOffset="50%" text-anchor="middle">UNLEASH ENGAGEMENT →</textPath></text>
  </g>

  <!-- Title block -->
  <g class="brand">
    <text class="brand-title" x="40" y="770">THE <tspan class="accent">ORVANE</tspan> FRAMEWORK</text>
    <text class="brand-tagline" x="42" y="792">LIBERATE THE WORKPLACE UNLEASHING VALUE THROUG PURPOSE AT EVERY LEVEL OF SCALE</text>
  </g>
</svg>
</body>
</html>
```